Non Propellant Static Eliminating Spray product needs a creative label design and logo

I need a label design that will speak for itself. I do not have a logo for the product name as it will just be part of the label design you come up with. The product is a static eliminating spray for all purpose use including hair, clothing, pets, all fabrics and can be used on just about anything. I would like to show somehow (maybe simple or line drawings of icons with staticy hair, pet, dress, pants ect.) Product name is "Cling Shield". This is my first product and only product as of right now. I will attach some info to maybe help with direction. I would like it to cater not only to the general public but to salons as well, if possible. I will need it to fit into the section where "Fuzz Ward and laundry items are sold (picture attached). Although most of the coloring in this section is blues,reds,yellow and oranges I would like it to have a slight stand out of a pop to have your eyes gravitate to my product. I'm thinking possible a darker bright blue or dark brighter Aqua/Teal. (attached pic for reference of color) Doesn't have to be these colors though. I would like some form of mild background and something making you think of static and blocking of static if possible. This must appeal to women and men. More women but a percentage of men as well so not too feminine and not masculine. My product is made from natural and naturally derived ingredients & is made in the USA. The product is "Patent Pending" & have a UPC also product name is in for Trademark so I will need TM. I am in the process of searching for a new bottle as I feel I need to compete with what's on the shelves currently. I am looking at either a white or black 8oz bottle with either a white or black or colored (possibly metallic finger sprayer with a cap on that) I may be using an over cap. Pictures are attached to give you a general idea. 8 oz bottle circumference will be about 1 7/8" to 2". I will update as soon as I know. I will also be having a 2oz or 3oz travel size as well. This bottle will not have an over cap, it will only have a finger sprayer with cap.
I am excited to see what you can come up with. Please feel free to be creative outside of anything I submitted. I'm still kind of at a loss of what I want but will know it when I see it. Please don't hesitate to contact me with any questions. Thank you for your help and your time.
Marla
Updates

I have updated my contest prize, I wasn't able to do the prize amount that I originally wanted to when I submitted for the job. Also, here are some dimensions and descriptions that I have updated. The dimensions of the label will be about 5.125". Bottle is white with either a white pump sprayer or black sprayer with a clear cap. Bottle is 8oz & dimensions are Total Hght: 6.16", Base Diameter 2.01", Circumference 6.375". I am going to be doing one continuous label. I will also be needing the label for a 2oz bottle as well. Please let me know if you need dimensions for that. My product name is also in for trademark and will need to have TM on it. Thank you to all participants and I am excited to see what you come up with.Marla Added Monday, November 16, 2015

Target Market(s)

Hearth Nest & More, Retail stores and Hair salons

Industry/Entity Type

Product

Requirements
Must have
• I will need some claims on the bottle. Hoping to be able to get a few on the front to let people know the benefits of my product going up against the only product on the market which has been around for 40 years but is not a good product at all.
• * Long Lasting
• * Non Flammable
• * Use on Hair, Clothes, Pets (maybe icons)
• * Natural & Naturally derived ingredients
• * All purpose Static Eliminator
• * Fresh Scent
Should not have
• Not a big fan of lightning rods or bolts unless mild enough to depict static. Fancy fonts.

```html
<!DOCTYPE html>
<html lang="en">
<head>
<meta charset="utf-8">
<title>Cling Shield – All Purpose Static Eliminator Label</title>
<link rel="stylesheet" href="https://fonts.googleapis.com/css2?family=Oswald:wght@600&family=Montserrat:wght@700;800&family=Roboto+Condensed:wght@400;500&display=swap">
<style>
  :root {
    --backdrop: #e4e5e6;
    --label-mint: #c9e2dc;
    --label-pale: #e9f3f0;
    --label-white: #f4f8f7;
    --teal: #2b8b74;
    --teal-soft: #6fb4a3;
    --teal-mist: #a8d3c8;
    --ink-teal: #1d6b58;
    --ink-dark: #1f3f37;
  }
  * { box-sizing: border-box; margin: 0; padding: 0; }
  html, body { width: 667px; height: 1200px; overflow: hidden; }
  body { background: var(--backdrop); position: relative; }

  .label {
    position: absolute; left: 190px; top: 258px; width: 290px; height: 850px;
    background: linear-gradient(180deg, var(--label-mint) 0%, var(--label-pale) 22%, var(--label-white) 40%, var(--label-white) 60%, var(--label-pale) 75%, var(--label-mint) 100%);
    overflow: hidden;
  }
  .band { position: absolute; left: 0; width: 100%; }
  .band--mist { background: var(--teal-mist); opacity: .55; }
  .band--soft { background: var(--teal-soft); opacity: .7; }
  .band--solid { background: var(--teal); }
  .block { position: absolute; background: var(--teal-mist); opacity: .5; }

  .brand-name {
    position: absolute; left: 0; width: 100%; top: 244px; text-align: center;
    font-family: "Oswald", sans-serif; font-weight: 600; color: var(--ink-teal);
    font-size: 94px; line-height: 88px; letter-spacing: -1px;
  }
  .brand-name .tm { font-size: 14px; vertical-align: top; line-height: 1; margin-left: 2px; }

  .tagline { position: absolute; left: 0; width: 100%; text-align: center; font-family: "Montserrat", sans-serif; color: var(--ink-dark); }
  .tagline--small { top: 474px; font-size: 12px; font-weight: 800; letter-spacing: .5px; }
  .tagline--main { top: 492px; font-size: 17px; font-weight: 800; letter-spacing: .6px; }

  .uses { position: absolute; left: 23px; top: 644px; width: 236px; height: 90px; }
  .uses svg { display: block; }

  .claims {
    position: absolute; left: 0; width: 100%; top: 752px; text-align: center;
    font-family: "Roboto Condensed", sans-serif; font-weight: 500; color: var(--ink-dark);
    font-size: 14.5px; line-height: 19px;
  }
  .net-weight {
    position: absolute; left: 0; width: 100%; top: 806px; text-align: center;
    font-family: "Roboto Condensed", sans-serif; font-weight: 400; color: var(--ink-dark);
    font-size: 17px;
  }
</style>
</head>
<body>
  <main class="label" aria-label="Cling Shield spray label">
    <div class="band band--mist" style="top:40px;height:18px"></div>
    <div class="block" style="left:70px;top:70px;width:180px;height:14px"></div>
    <div class="block" style="left:20px;top:96px;width:240px;height:10px"></div>
    <div class="band band--mist" style="top:120px;height:22px"></div>
    <div class="band band--soft" style="top:160px;height:12px"></div>
    <div class="band band--solid" style="top:182px;height:22px"></div>
    <div class="band band--soft" style="top:210px;height:8px"></div>

    <h1 class="brand-name">CLING<br>SHIELD<span class="tm">TM</span></h1>
    <p class="tagline tagline--small">ALL PURPOSE</p>
    <p class="tagline tagline--main">STATIC ELIMINATOR</p>

    <div class="band band--soft" style="top:524px;height:10px"></div>
    <div class="band band--solid" style="top:538px;height:18px"></div>
    <div class="band band--soft" style="top:562px;height:14px"></div>
    <div class="block" style="left:0;top:586px;width:210px;height:10px"></div>
    <div class="band band--mist" style="top:604px;height:14px"></div>

    <section class="uses" aria-label="Uses: hair, clothes, pets">
      <svg width="236" height="90" viewBox="0 0 236 90">
        <defs>
          <path id="arc-hair" d="M6 58 A26 26 0 0 1 58 58"/>
          <path id="arc-clothes" d="M92 58 A26 26 0 0 1 144 58"/>
          <path id="arc-pets" d="M177 58 A26 26 0 0 1 229 58"/>
        </defs>
        <rect x="0.75" y="8" width="234.5" height="78" rx="6" fill="none" stroke="#1f3f37" stroke-width="1.3"/>
        <rect x="90" y="2" width="56" height="13" fill="#e3f0ec"/>
        <text x="118" y="12.5" text-anchor="middle" font-family="Montserrat, sans-serif" font-weight="800" font-size="10" fill="#1f3f37" letter-spacing=".5">USES</text>
        <g font-family="Montserrat, sans-serif" font-weight="700" font-size="6.5" fill="#1f3f37" letter-spacing=".4">
          <text><textPath href="#arc-hair" startOffset="50%" text-anchor="middle">HAIRS</textPath></text>
          <text><textPath href="#arc-clothes" startOffset="50%" text-anchor="middle">CLOTHES</textPath></text>
          <text><textPath href="#arc-pets" startOffset="50%" text-anchor="middle">PETS</textPath></text>
        </g>
        <circle cx="32" cy="58" r="21" fill="#f4f8f7" stroke="#1f3f37" stroke-width="1.5"/>
        <circle cx="32" cy="58" r="16" fill="#1f3f37" role="img" aria-label="Icon of voluminous hair"/>
        <circle cx="118" cy="58" r="21" fill="#f4f8f7" stroke="#1f3f37" stroke-width="1.5"/>
        <circle cx="118" cy="58" r="16" fill="#1f3f37" role="img" aria-label="Icon of a shirt"/>
        <circle cx="203" cy="58" r="21" fill="#f4f8f7" stroke="#1f3f37" stroke-width="1.5"/>
        <circle cx="203" cy="58" r="16" fill="#1f3f37" role="img" aria-label="Icon of a dog and cat"/>
      </svg>
    </section>

    <p class="claims">Long Lasting | Non Flammable<br>Natural Ingredients | Fresh Scent</p>
    <p class="net-weight">NET WT 8.2 OZ (186g)</p>
  </main>
</body>
</html>
```